Elite Company Card

create a new dark colored, with metallic accents business card that people will not want to throw away

prefer rounded corners

Font styles to use
Serif

Requirements
Must have
• metallic accents
Nice to have
• 2 sided, the company logo prominent on one side the person and company info on the other side
Should not have
• no white

```html
<!DOCTYPE html>
<html lang="en">
<head>
<meta charset="utf-8">
<title>Keystone Autobody &amp; Paint Works — Business Card</title>
<link rel="stylesheet" href="https://fonts.googleapis.com/css2?family=Lora:ital,wght@0,400;0,700;1,400&display=swap">
<style>
  :root {
    --navy-deep: #13306a;
    --navy: #1d4a8f;
    --navy-light: #2e68b3;
    --steel-dark: #6f7780;
    --steel: #aeb5be;
    --steel-light: #d3d8de;
    --ink-light: #f1f3f6;
    --backdrop: #e9e6e1;
  }
  html, body {
    margin: 0;
    width: 1200px;
    height: 1024px;
    overflow: hidden;
    background: var(--backdrop);
    font-family: "Lora", Georgia, serif;
  }
  .sheet { position: relative; width: 1200px; height: 1024px; }
  .card {
    position: absolute;
    left: 180px;
    width: 840px;
    height: 480px;
    border-radius: 40px;
    overflow: hidden;
    box-shadow: 0 10px 26px rgba(0,0,0,0.22);
  }
  .card--front { top: 20px; background: var(--steel); }
  .card--back {
    top: 524px;
    background: radial-gradient(ellipse at 55% 45%, var(--navy-light) 0%, var(--navy) 45%, var(--navy-deep) 100%);
  }
  .card__art { position: absolute; inset: 0; width: 100%; height: 100%; }

  .brand {
    position: absolute;
    display: flex;
    align-items: center;
    gap: 14px;
    font-weight: 700;
    text-transform: uppercase;
    line-height: 1.2;
  }
  .brand__dot { flex: none; border-radius: 50%; }
  .card--front .brand {
    left: 54px;
    top: 276px;
    color: var(--navy-deep);
    font-size: 22px;
  }
  .card--front .brand__dot { width: 22px; height: 22px; background: var(--navy-deep); }
  .card--back .brand {
    left: 0;
    right: 0;
    top: 170px;
    justify-content: center;
    color: var(--ink-light);
    font-size: 30px;
  }
  .card--back .brand__dot { width: 28px; height: 28px; background: var(--steel-light); }

  .details { position: absolute; left: 470px; top: 42px; color: var(--ink-light); }
  .details__name { margin: 0; font-size: 27px; font-weight: 700; letter-spacing: 0.5px; }
  .details__title { margin: 2px 0 22px; font-size: 16px; font-weight: 400; text-transform: uppercase; }
  .details__address { margin: 0 0 26px; font-size: 17px; line-height: 1.35; font-style: normal; }
  .contact-list { list-style: none; margin: 0; padding: 0; font-size: 16px; }
  .contact-list li { display: flex; align-items: center; gap: 12px; height: 27px; }
  .contact-list svg { width: 16px; height: 16px; flex: none; }
  .web-line {
    position: absolute;
    left: 52px;
    bottom: 38px;
    margin: 0;
    color: var(--ink-light);
    font-size: 17px;
    font-style: italic;
  }
</style>
</head>
<body>
<main class="sheet">

  <section class="card card--front" aria-label="Card front">
    <svg class="card__art" viewBox="0 0 840 480" preserveAspectRatio="none" aria-hidden="true">
      <defs>
        <linearGradient id="front-steel" x1="0" y1="0" x2="1" y2="1">
          <stop offset="0" stop-color="#c7cdd4"/>
          <stop offset="0.5" stop-color="#aeb5be"/>
          <stop offset="1" stop-color="#8d949d"/>
        </linearGradient>
        <linearGradient id="front-navy" x1="0" y1="0" x2="1" y2="1">
          <stop offset="0" stop-color="#2a5ea8"/>
          <stop offset="0.6" stop-color="#1d4a8f"/>
          <stop offset="1" stop-color="#13306a"/>
        </linearGradient>
        <linearGradient id="front-chrome" x1="0" y1="0" x2="1" y2="0">
          <stop offset="0" stop-color="#e4e8ec"/>
          <stop offset="0.35" stop-color="#6f7780"/>
          <stop offset="0.6" stop-color="#eef1f4"/>
          <stop offset="1" stop-color="#7d858e"/>
        </linearGradient>
      </defs>
      <rect width="840" height="480" fill="url(#front-steel)"/>
      <path d="M0 0 H840 V480 H430 C380 330 300 230 200 200 C120 176 60 170 0 168 Z" fill="url(#front-navy)"/>
      <path class="chrome-swoosh" d="M0 160 C70 162 140 170 210 196 C310 232 390 330 440 480 L410 480 C360 340 290 250 200 220 C130 196 70 190 0 188 Z" fill="url(#front-chrome)"/>
    </svg>

    <div class="brand"><span class="brand__dot"></span><span>Keystone<br>Autobody &amp;<br>Paint Works</span></div>

    <div class="details">
      <h1 class="details__name">MARCUS HALE</h1>
      <p class="details__title">Job Title</p>
      <address class="details__address">48 Harbor Lane, PO Box 902,<br>Millbrook Q 4410,<br>California</address>
      <ul class="contact-list">
        <li><svg viewBox="0 0 16 16"><path d="M3 1h3l1 4-2 1c1 2 3 4 5 5l1-2 4 1v3c0 1-1 2-2 2C7 15 1 9 1 3c0-1 1-2 2-2z" fill="#f1f3f6"/></svg>0455 381 720</li>
        <li><svg viewBox="0 0 16 16"><rect x="4" y="1" width="8" height="14" rx="1.5" fill="none" stroke="#f1f3f6" stroke-width="1.6"/></svg>07 5540 2100</li>
        <li><svg viewBox="0 0 16 16"><rect x="2" y="6" width="12" height="7" fill="#f1f3f6"/><rect x="4" y="2" width="8" height="4" fill="none" stroke="#f1f3f6" stroke-width="1.4"/></svg>07 5540 2199</li>
        <li><svg viewBox="0 0 16 16"><rect x="1" y="3" width="14" height="10" fill="none" stroke="#f1f3f6" stroke-width="1.6"/><path d="M1 3l7 6 7-6" fill="none" stroke="#f1f3f6" stroke-width="1.4"/></svg>marcus@keystoneautobody.com</li>
        <li><svg viewBox="0 0 16 16"><circle cx="8" cy="8" r="6.5" fill="none" stroke="#f1f3f6" stroke-width="1.5"/><path d="M1.5 8h13M8 1.5c-3 3-3 10 0 13M8 1.5c3 3 3 10 0 13" fill="none" stroke="#f1f3f6" stroke-width="1.2"/></svg>www.keystoneautobody.com</li>
      </ul>
    </div>
  </section>

  <section class="card card--back" aria-label="Card back">
    <div class="brand"><span class="brand__dot"></span><span>Keystone<br>Autobody &amp;<br>Paint Works</span></div>
    <p class="web-line">www.keystoneautobody.com</p>
  </section>

</main>
</body>
</html>
```